Yoga By Marisol Ad for print

I need a print ad designed to go in a brochure for a charity event. I've attached the specs. I need the specs for the 1/2 page ad.
Text for ad:

“E-RYT 200 extensive training with Asana Scholars
Social Media Influencer
Offering group, private and corporate yoga classes
Email: info@yogabymarisol-studio.com
Web: www.yogabymarisol-studio.com
Phone: 480-555-0163
Instagram: @flowofmarisol

Target Market(s)

Yoga practitioners and businesses looking to bring yoga in to their operation.

Font styles to use
Serif
Script

Colors
eda3c7
e34197
eea4c8
f9d9e8
feeeee
000000
1b1b1b
cbcbcb
eaeaea

Requirements
Must have
• One version of my logo, I have provided many to choose from for best aesthetic appeal

```html
<!DOCTYPE html>
<html lang="en">
<head>
<meta charset="utf-8">
<title>Yoga By Marisol – Print Ad</title>
<link rel="stylesheet" href="https://fonts.googleapis.com/css2?family=Cormorant+Garamond:wght@300;400;500&family=Great+Vibes&display=swap">
<style>
  :root {
    --backdrop: #0f7d83;
    --pink-light: #fcdcec;
    --pink-mid: #f6b3d6;
    --pink-edge: #f099c6;
    --accent: #e34197;
    --footer: #a1356f;
    --ink: #1b1b1b;
    --ink-soft: #3a3a3a;
    --white: #ffffff;
  }
  * { box-sizing: border-box; margin: 0; padding: 0; }
  html, body {
    width: 1200px; height: 2400px; overflow: hidden;
    background: var(--backdrop);
  }
  .ad {
    position: absolute; left: 100px; top: 540px;
    width: 1000px; height: 1320px; overflow: hidden;
    background: radial-gradient(ellipse at 55% 45%, var(--pink-light) 0%, var(--pink-mid) 60%, var(--pink-edge) 100%);
    font-family: "Cormorant Garamond", Georgia, serif;
    box-shadow: 0 10px 30px rgba(0,0,0,0.25);
  }
  .ad__title {
    position: absolute; left: 72px; top: 90px;
    font-weight: 300; font-size: 100px; line-height: 150px;
    color: var(--ink); letter-spacing: 2px; text-transform: uppercase;
  }
  .ad__title-script {
    font-family: "Great Vibes", cursive;
    text-transform: none; font-size: 104px; letter-spacing: 0;
  }
  .brand {
    position: absolute; left: 620px; top: 235px; width: 330px;
    display: flex; align-items: center; justify-content: center; gap: 14px;
  }
  .brand__dot { width: 24px; height: 24px; border-radius: 50%; background: var(--accent); }
  .brand__name { font-weight: 500; font-size: 56px; color: var(--accent); }
  .portrait {
    position: absolute; left: 630px; top: 470px; width: 310px; height: 560px;
    background: linear-gradient(180deg, rgba(238,196,170,0.35) 0%, rgba(238,196,170,0.6) 30%, rgba(244,128,110,0.6) 55%, rgba(176,52,120,0.75) 100%);
    border-radius: 150px 150px 30px 30px;
  }
  .portrait-base {
    position: absolute; left: 500px; top: 1000px; width: 470px; height: 150px;
    background: linear-gradient(180deg, rgba(176,52,120,0.75), rgba(176,52,120,0.9));
    border-radius: 70px 70px 20px 20px;
  }
  .features { position: absolute; left: 0; top: 575px; width: 610px; list-style: none; }
  .feature {
    display: flex; align-items: center; gap: 24px;
    padding: 14px 0 14px 72px; margin-bottom: 30px; min-height: 110px;
    background: linear-gradient(90deg, rgba(255,255,255,0.45) 0%, rgba(255,255,255,0.3) 70%, rgba(255,255,255,0) 100%);
    font-weight: 500; font-size: 36px; line-height: 42px; color: var(--ink-soft);
  }
  .feature__icon { flex: none; width: 24px; height: 24px; }
  .footer {
    position: absolute; left: 0; bottom: 0; width: 100%; height: 170px;
    background: var(--footer); color: var(--white);
    display: flex; flex-direction: column; align-items: center; justify-content: center;
    font-weight: 500; font-size: 30px; line-height: 46px;
  }
  .footer__row { display: flex; gap: 18px; }
</style>
</head>
<body>
  <section class="ad">
    <h1 class="ad__title">Yoga<br><span class="ad__title-script">By</span><br>Marisol</h1>

    <div class="brand">
      <span class="brand__dot"></span>
      <span class="brand__name">Flow Atelier</span>
    </div>

    <div class="portrait" role="img" aria-label="Photo of the instructor seated cross-legged, arms stretched overhead, in a coral top and magenta leggings"></div>
    <div class="portrait-base" role="img" aria-label="Instructor's crossed legs in magenta leggings"></div>

    <ul class="features">
      <li class="feature">
        <svg class="feature__icon" viewBox="0 0 26 26"><path d="M6 4 L18 13 L6 22" fill="none" stroke="#e34197" stroke-width="4" stroke-linecap="round" stroke-linejoin="round"/></svg>
        <span>E-RYT 200 Trained with<br>Asana Scholars</span>
      </li>
      <li class="feature">
        <svg class="feature__icon" viewBox="0 0 26 26"><path d="M6 4 L18 13 L6 22" fill="none" stroke="#e34197" stroke-width="4" stroke-linecap="round" stroke-linejoin="round"/></svg>
        <span>Social Media Influencer</span>
      </li>
      <li class="feature">
        <svg class="feature__icon" viewBox="0 0 26 26"><path d="M6 4 L18 13 L6 22" fill="none" stroke="#e34197" stroke-width="4" stroke-linecap="round" stroke-linejoin="round"/></svg>
        <span>Group, Private and<br>Corporate Yoga Classes</span>
      </li>
    </ul>

    <footer class="footer">
      <div class="footer__row">
        <span>E: info@yogabymarisol-studio.com</span><span>|</span><span>W: www.yogabymarisol-studio.com</span>
      </div>
      <div class="footer__row">
        <span>P: 480-555-0163</span><span>|</span><span>IG: @flowofmarisol</span>
      </div>
    </footer>
  </section>
</body>
</html>
```